Webdesign für Brenner Flusstrom
Zielgruppe
Ansprechpartner für Planung und Errichtung von Stromerzeugung durch erneuerbare Energien. Alle Interessen im privaten, teilöffentlichen und öffentlichen Bereich, die mittel- und langfristig umweltschonenden Strom nutzen wollen.
Aufgabenstellung
- Farben bitte in den Unternehmensfarben Blau/Weiß mit einem kleinen Anteil Orange
- Bilder nach Möglichkeit bitte nur eigene (siehe Anhang)
- klare und übersichtliche Struktur
- KEIN Abklatsch der alten Webseite

```html
<!DOCTYPE html>
<html lang="de">
<head>
<meta charset="utf-8">
<title>Energietechnik Brenner</title>
<link rel="stylesheet" href="https://fonts.googleapis.com/css2?family=Oswald:wght@400;500;600;700&family=Open+Sans:wght@400;600&display=swap">
<style>
:root{
  --navy:#09097f;
  --navy-dark:#05055e;
  --orange:#ee8a0a;
  --ink:#111118;
  --text:#2b2b33;
  --line:#1a1a40;
  --white:#ffffff;
}
*{box-sizing:border-box;margin:0;padding:0}
html,body{width:1200px;height:4147px;overflow:hidden;background:var(--white)}
body{position:relative;font-family:"Open Sans",Arial,sans-serif;color:var(--text)}
.abs{position:absolute}
.display{font-family:"Oswald",Arial,sans-serif;font-weight:600;color:var(--ink);text-transform:uppercase;letter-spacing:.5px;line-height:1.15}
.eyebrow{font-family:"Oswald",Arial,sans-serif;font-weight:400;font-size:16px;color:var(--orange);text-transform:uppercase}
.lead{font-family:"Oswald",Arial,sans-serif;font-weight:500;font-size:18px;color:var(--ink);line-height:1.5}
.copy{font-size:17px;line-height:1.45;color:var(--text)}
.btn{position:absolute;display:flex;align-items:center;justify-content:center;border-radius:22px;background:var(--navy);color:var(--white);font-family:"Oswald",Arial,sans-serif;font-weight:500;font-size:16px;text-decoration:none}
.brand-name{font-family:"Oswald",Arial,sans-serif;font-weight:600;color:var(--navy);font-size:18px;line-height:1.05;text-transform:uppercase}

/* header */
.main-nav a{position:absolute;top:48px;font-family:"Oswald",Arial,sans-serif;font-size:18px;color:var(--ink);text-decoration:none;white-space:nowrap}
.hero-title{left:114px;top:158px;font-size:44px}
.hero-text{left:114px;top:226px;width:380px;font-size:19px;line-height:1.45;color:var(--text)}
.cert-badge{left:114px;top:472px;width:86px;height:86px;border-radius:50%;background:#f2f2f2;border:3px solid #e03a2f}

/* about */
.about-photo{left:0;top:746px;width:524px;height:562px;border-radius:0 6px 6px 0;background:linear-gradient(160deg,#3d4a3a,#1f2a24 55%,#4f6f9a)}
.about-text{left:565px;width:530px}

/* partner */
.partner-name{left:106px;top:1556px;font-family:"Oswald",Arial,sans-serif;font-weight:600;font-size:34px;color:var(--navy)}
.partner-title{left:548px;top:1420px;font-size:42px;color:var(--white)}
.partner-lead{left:548px;top:1555px;width:520px;color:var(--white)}
.partner-lead a{color:var(--orange)}
.partner-copy{left:548px;top:1598px;width:470px;color:var(--white);font-size:17px}

/* services */
.service-card{position:absolute;top:2086px;width:298px;height:424px;border-radius:6px;overflow:hidden;background:linear-gradient(180deg,#6b7aa8,#3f3aa0 55%,#2c24a0)}
.service-card h3{position:absolute;left:15px;top:248px;font-family:"Oswald",Arial,sans-serif;font-weight:600;font-size:29px;color:var(--white);text-transform:uppercase}
.service-card p{position:absolute;left:15px;top:302px;width:272px;font-size:16px;line-height:1.65;color:var(--white);letter-spacing:-.4px}

/* career */
.career-band{left:0;top:2582px;width:1200px;height:497px;background:linear-gradient(90deg,#4a4c7a,#2e3060 50%,#232552)}

/* contact */
.field{position:absolute;border-bottom:1.5px solid var(--line);font-size:16px;color:#555;padding-bottom:6px}
.info-title{font-family:"Oswald",Arial,sans-serif;font-weight:500;font-size:18px;color:var(--ink)}
.info-text{font-size:17px;color:var(--text)}

/* footer */
.site-footer{left:0;top:3807px;width:1200px;height:317px;background:var(--navy)}
.footer-col h4{font-family:"Oswald",Arial,sans-serif;font-weight:500;font-size:16px;color:var(--white)}
.footer-col p{font-size:14px;color:var(--white);letter-spacing:-.3px;margin-bottom:14px}
.footer-links a{position:absolute;left:891px;font-family:"Oswald",Arial,sans-serif;font-weight:500;font-size:17px;color:var(--white);text-decoration:none}
.bottom-bar{left:0;top:4124px;width:1200px;height:23px;background:#0a0a14;color:var(--white);font-size:11px;text-align:center;line-height:23px}
</style>
</head>
<body>

<!-- Header / Hero -->
<svg class="abs" style="left:0;top:0" width="1200" height="676" viewBox="0 0 1200 676" role="img" aria-label="Foto: Monteur installiert Solarmodule auf einem Flachdach">
  <defs>
    <linearGradient id="heroFill" x1="0" y1="0" x2="0" y2="1">
      <stop offset="0" stop-color="#9fb4d6"/>
      <stop offset=".45" stop-color="#7b8fa3"/>
      <stop offset="1" stop-color="#b8bcc4"/>
    </linearGradient>
  </defs>
  <path d="M370 0 L926 0 L1200 300 L1200 673 L242 673 L600 250 Q636 210 600 170 Z" fill="url(#heroFill)"/>
  <path d="M982 0 L1200 0 L1200 60 Z" fill="url(#heroFill)"/>
</svg>

<div class="abs" style="left:113px;top:28px;display:flex;align-items:center;gap:8px">
  <span style="width:14px;height:14px;border-radius:50%;background:var(--navy)"></span>
  <span class="brand-name">Brenner<br>Flusstrom</span>
</div>

<nav class="main-nav">
  <a style="left:568px">Home</a>
  <a style="left:656px">Unternehmen</a>
  <a style="left:798px">Leistungen ⌄</a>
  <a style="left:922px">Referenzen</a>
  <a style="left:1048px">Kontakt</a>
</nav>

<h1 class="abs display hero-title">Energietechnik Brenner</h1>
<p class="abs hero-text">Ihr Ansprechpartner für Planung und Errichtung von Stromerzeugung durch erneuerbare Energien.<br><br>Kontaktieren Sie uns jetzt und starten Sie Ihre Reise zu nachhaltiger Energie!</p>
<a class="btn" style="left:114px;top:409px;width:255px;height:44px">Jetzt Kontakt aufnehmen</a>
<div class="abs cert-badge"></div>

<!-- About -->
<div class="abs about-photo" role="img" aria-label="Foto: die beiden Inhaber vor grünem Laub"></div>
<p class="abs eyebrow" style="left:565px;top:772px">Das sind wir</p>
<h2 class="abs display" style="left:565px;top:808px;font-size:42px">Über das Unternehmen</h2>
<p class="abs lead about-text" style="top:882px;font-size:18px;line-height:1.5">Mit über 30 Jahren Erfahrung in der Planung und Errichtung von erneuerbare Energien Anlagen sind wir Ihre Ansprechpartner wenn es um die Stromerzeugung und Sektor Kopplung geht.</p>
<p class="abs copy about-text" style="top:980px">Durch unsere große Erfahrung im Bereich des Energiebaus und der erneuerbaren Energien haben Sie mit uns ein leistungsfähiges Unternehmen für Ihre Projekte an der Hand. Sprechen Sie uns einfach für Ihre Projekte an, wir stehen von der Ingenieurplanung, über die Ausführung, bis hin zur Betriebsführung an Ihrer Seite.<br><br>Als Familienunternehmen in zweiter Generation finden Sie bei uns kurze Wege, hohe qualitative Leistungen und einen großenErfahrungsschatz.</p>
<a class="btn" style="left:565px;top:1244px;width:307px;height:42px">Mehr über unser Unternehmen</a>

<!-- Partner -->
<svg class="abs" style="left:0;top:1379px" width="1200" height="406" viewBox="0 856 745 252" preserveAspectRatio="none" aria-hidden="true">
  <path d="M98 1108 L340 856 L745 856 L745 1108 Z" fill="var(--navy)"/>
  <path d="M145 856 L330 856 L262 924 Q235 948 208 924 Z" fill="var(--navy)"/>
  <path d="M628 856 L745 968" stroke="#fff" stroke-width="9"/>
</svg>
<p class="abs partner-name">Solvanta</p>
<h2 class="abs display partner-title">Pemiumpartnerschaft<br>mit Solvanta</h2>
<p class="abs lead partner-lead" style="color:var(--white)">Brenner Flusstrom ist stolzer Premiumpartner von <a>Solvanta</a></p>
<p class="abs copy partner-copy">Brenner Flusstrom ist mit Stolz ein Premiumpartner von Solvanta, einem führenden Unternehmen im Bereich innovativer und nachhaltiger Photovoltaik-Technologie. Unsere Partnerschaft unterstützt die gemeinsame Vision einer sauberen und nachhaltigen Zukunft, in der erneuerbare Energien eine zentrale Rolle spielen.</p>

<!-- Services -->
<p class="abs eyebrow" style="left:106px;top:1858px">Unsere Angebote für eine nachhaltige Zukunft</p>
<h2 class="abs display" style="left:106px;top:1893px;font-size:42px">Unsere Leistungen</h2>
<p class="abs lead" style="left:106px;top:1968px">Wir bieten Ihnen nachhaltige Lösungen im Bereich Wasserkraft, Photovoltaik und E-Mobilität</p>
<p class="abs copy" style="left:106px;top:2003px;width:1000px">Brenner Flusstrom setzt Maßstäbe in den Bereichen Wasserkraft, Photovoltaik und E-Mobilität. Erfahren Sie mehr über unsere nachhaltigen Lösungen und wie sie die Umwelt positiv beeinflussen.</p>

<div class="service-card" style="left:106px" role="img" aria-label="Foto: Wehr an einem Fluss">
  <h3>Wasserkraft</h3>
  <p>Seit 25 Jahren sind wir Ihr kompetenter Ansprechpartner in Sachen Planung, Errichtung und Betrieb von Wasserkraftanlagen.</p>
</div>
<div class="service-card" style="left:451px" role="img" aria-label="Foto: Solarpark unter Himmel">
  <h3>Photovoltaik</h3>
  <p>Als Experten im Bereich regenerative Energien finden Sie mit uns Ihren Partner zur Verwirklichung Ihrer Photovoltaikprojekte.</p>
</div>
<div class="service-card" style="left:796px" role="img" aria-label="Foto: Ladesäule für Elektrofahrzeuge">
  <h3>E-Mobilität</h3>
  <p>Wir bieten Ihnen Testfahrten in Elektrofahrzeugen, Langzeitmieten und die Errichtung von Elektroladeparkplätzen an.</p>
</div>

<!-- Career -->
<div class="abs career-band" role="img" aria-label="Foto: zwei Teammitglieder sitzen vor einer Hecke"></div>
<p class="abs eyebrow" style="left:530px;top:2657px">Werde Teil unseres Teams</p>
<h2 class="abs display" style="left:530px;top:2692px;font-size:42px;color:var(--white)">Karriere bei<br>Energietechnik Brenner</h2>
<p class="abs lead" style="left:530px;top:2820px;width:560px;color:var(--white)">Schließen Sie sich unserem Team an und gestalten Sie die Zukunft der umweltschonenden Stromerzeugung.</p>
<p class="abs copy" style="left:530px;top:2888px;width:520px;color:var(--white);font-size:16px;letter-spacing:-.3px">Bei Energietechnik Brenner finden Sie vielfältige Möglichkeiten, Ihre Leidenschaft für erneuerbare Energien in die Tat umzusetzen.</p>
<a class="btn" style="left:530px;top:2967px;width:271px;height:42px;background:var(--white);color:var(--navy)">Zu den Stellenangeboten</a>

<!-- Contact -->
<p class="abs eyebrow" style="left:106px;top:3151px">Ihre Anliegen im Fokus</p>
<h2 class="abs display" style="left:106px;top:3188px;font-size:42px">Wir freuen uns von Ihnen zu hören!</h2>
<p class="abs lead" style="left:106px;top:3265px">Sie benötigen Unterstützung? Nehmen Sie jetzt Kontakt mit uns auf! Wir freuen uns auf Ihre Nachricht und werden uns bemühen,</p>
<p class="abs copy" style="left:106px;top:3302px;width:1000px">Unsere engagierte Team steht Ihnen zur Verfügung, um Ihre Fragen zu Wasserkraft, Photovoltaik, und E-Mobilität zu beantworten. Kontaktieren Sie uns und lassen Sie uns gemeinsam an einer nachhaltigen Zukunft arbeiten.</p>

<form>
  <p class="abs info-title" style="left:106px;top:3412px">Kontaktformular</p>
  <div class="field" style="left:106px;top:3460px;width:237px">Name</div>
  <div class="field" style="left:358px;top:3460px;width:236px">E-Mail</div>
  <div class="field" style="left:106px;top:3512px;width:237px">Anliegen<span style="position:absolute;right:6px">⌄</span></div>
  <div class="field" style="left:358px;top:3512px;width:236px;border:none">Telefonnummer (optional)</div>
  <div class="field" style="left:106px;top:3572px;width:488px;height:101px">Nachricht</div>
  <a class="btn" style="left:387px;top:3696px;width:207px;height:40px">Nachricht senden</a>
</form>

<svg class="abs" style="left:708px;top:3412px" width="26" height="200" viewBox="0 0 26 200" aria-hidden="true">
  <path d="M5 3 L10 3 L12 9 L9 11 Q12 17 16 19 L18 16 L24 18 L24 23 Q22 25 18 25 Q4 22 2 7 Q2 3 5 3 Z" fill="var(--ink)"/>
  <circle cx="13" cy="93" r="10" fill="none" stroke="var(--ink)" stroke-width="2"/>
  <path d="M13 87 L13 93 L17 96" fill="none" stroke="var(--ink)" stroke-width="2"/>
  <path d="M13 162 C6 162 3 167 3 171 C3 178 13 188 13 188 C13 188 23 178 23 171 C23 167 20 162 13 162 Z" fill="var(--ink)"/>
  <circle cx="13" cy="171" r="3.5" fill="#fff"/>
</svg>
<p class="abs info-title" style="left:748px;top:3412px">Telefon</p>
<p class="abs info-text" style="left:748px;top:3450px;color:var(--orange);text-decoration:underline">03725 / 4810</p>
<p class="abs info-title" style="left:748px;top:3492px">Öffnungszeiten</p>
<p class="abs info-text" style="left:748px;top:3531px">Montag - Freitag 7:00 - 18:00 Uhr</p>
<p class="abs info-title" style="left:748px;top:3573px">Adresse</p>
<p class="abs info-text" style="left:750px;top:3611px">Ahornweg 14, 09120 Talheim</p>

<!-- Footer -->
<footer class="abs site-footer">
  <div class="abs" style="left:205px;top:135px;display:flex;align-items:center;gap:8px">
    <span style="width:14px;height:14px;border-radius:50%;background:var(--white)"></span>
    <span class="brand-name" style="color:var(--white)">Brenner<br>Flusstrom</span>
  </div>
  <div class="abs footer-col" style="left:488px;top:77px">
    <h4>Adresse</h4><p>Ahornweg 14, 09120 Talheim</p>
    <h4>Öffnungszeiten</h4><p>Montag - Freitag 7:00 - 18:00 Uhr</p>
    <h4>Telefon</h4><p>03725 / 4810</p>
  </div>
  <nav class="footer-links">
    <a style="top:83px">Kontakt</a>
    <a style="top:127px">Karriere</a>
    <a style="top:171px">Impressum</a>
    <a style="top:215px">Datenschutz</a>
  </nav>
</footer>
<div class="abs bottom-bar">© 2023 - Brenner Energietechnik Talheim| All rights reserved</div>

</body>
</html>
```